Business Card Design

I am a mental health counselor in private practice. I provide counseling to individuals, couples, and adults. There is a design on CardLoom that I really like. It is 2 talking bubbles joined together by a heart. That is just a suggestion. I'm interested in other ideas. I would like my photo to be on the back of the card, along with the text Miriam Delacott Counseling. I would like mint green as my background color and navy writing, if possible. The final design should be elegant, professional, and maybe just a touch whimsical.
Target Market(s)
Individual adolescents, adults, couples, and families seeking counseling.
Industry/Entity Type
Mental Health
Contact Information for Business Card
Miriam Delacott
A Compassionate Path to Healing
Miriam Delacott, M.S. NCC
Wexmoor Hall
2947 NW Calloway Street, Suite 318
Portland OR 97209
503-286-1573
counselingwithmiriam-example.com
Requirements
Must have
- The card must have all of the text provided and my photo.
Nice to have
- I like cards that are rounded on the sides, and I like thick paper.

```html
<!DOCTYPE html>
<html lang="en">
<head>
<meta charset="utf-8">
<title>Miriam Delacott Counseling – Business Card</title>
<link href="https://fonts.googleapis.com/css2?family=Saira+Condensed:wght@400;500;700&display=swap" rel="stylesheet">
<style>
  :root {
    --page: #ece9e3;
    --mint-light: #a9de98;
    --mint: #8fd07c;
    --mint-deep: #7cc46a;
    --ink: #ffffff;
    --ink-soft: rgba(255,255,255,0.85);
    --photo-a: #c9c2b8;
    --photo-b: #6f6a66;
    --shadow: rgba(0,0,0,0.18);
  }
  * { margin: 0; padding: 0; box-sizing: border-box; }
  html, body {
    width: 1200px; height: 1000px; overflow: hidden;
    background: var(--page);
    font-family: "Saira Condensed", "Arial Narrow", sans-serif;
    color: var(--ink);
  }
  .card {
    position: absolute;
    width: 760px; height: 440px;
    left: 220px;
    border-radius: 30px;
    overflow: hidden;
    background: linear-gradient(135deg, var(--mint-light), var(--mint) 55%, var(--mint-deep));
    box-shadow: 0 10px 28px var(--shadow);
  }
  .card--profile { top: 50px; }
  .card--brand { top: 520px; }

  /* profile side */
  .profile-photo {
    position: absolute; left: 0; top: 0;
    width: 330px; height: 440px;
    background: linear-gradient(160deg, var(--photo-a), var(--photo-b));
    clip-path: ellipse(100% 78% at 0% 50%);
  }
  .profile-photo-rim {
    position: absolute; left: 0; top: 0;
    width: 340px; height: 440px;
    background: rgba(255,255,255,0.55);
    clip-path: ellipse(100% 78% at 0% 50%);
  }
  .profile-info {
    position: absolute; left: 380px; top: 42px; right: 36px;
  }
  .person-name {
    font-weight: 700; font-size: 40px; letter-spacing: 1.5px;
    text-transform: uppercase; line-height: 1;
  }
  .person-title {
    font-weight: 400; font-size: 22px; color: var(--ink-soft);
    margin-top: 4px;
  }
  .practice-mark {
    display: flex; align-items: center; gap: 12px;
    margin-top: 30px;
  }
  .practice-mark-dot {
    width: 30px; height: 30px; border-radius: 50%;
    border: 2px solid var(--ink-soft);
    flex: none;
  }
  .practice-mark-name {
    font-weight: 500; font-size: 17px; letter-spacing: 1.5px;
    text-transform: uppercase; line-height: 1.2;
  }
  .contact { margin-top: 34px; font-size: 19px; line-height: 1.35; }
  .contact-phone { font-size: 24px; letter-spacing: 2px; margin-bottom: 12px; }

  /* brand side */
  .brand-text {
    position: absolute; left: 0; right: 0; top: 0; bottom: 0;
    display: flex; flex-direction: column; justify-content: center;
    padding-left: 90px;
  }
  .brand-tagline {
    font-weight: 500; font-size: 28px; letter-spacing: 2px;
    text-transform: uppercase;
  }
  .brand-name {
    font-weight: 700; font-size: 46px; letter-spacing: 2px;
    text-transform: uppercase; margin-top: 6px; line-height: 1.1;
  }
</style>
</head>
<body>
  <section class="card card--profile">
    <div class="profile-photo-rim"></div>
    <div class="profile-photo" role="img" aria-label="Portrait photo of the counselor smiling in front of a bookshelf"></div>
    <div class="profile-info">
      <h1 class="person-name">Miriam Delacott</h1>
      <p class="person-title">Mental health counselor</p>
      <div class="practice-mark">
        <span class="practice-mark-dot"></span>
        <span class="practice-mark-name">A Compassionate<br>Path to Healing</span>
      </div>
      <div class="contact">
        <p class="contact-phone">503 - 286 - 1573</p>
        <p>www.counselingwithmiriam-example.com</p>
        <p>M.S. NCC Wexmoor Hall 2947 NW</p>
        <p>Calloway Street Suite 318</p>
        <p>Portland OR 97209</p>
      </div>
    </div>
  </section>

  <section class="card card--brand">
    <div class="brand-text">
      <p class="brand-tagline">A Compassionate Path to Healing</p>
      <h2 class="brand-name">Miriam Delacott</h2>
    </div>
  </section>
</body>
</html>
```